Creative Web Design for an ERP (technology) Consulting Business

I need two pages designed for the ERP Project Management Consulting Company I am starting. One page is the home page, the other page is an important inside page.

I've looked at many different templates for sites like this, and they all look the same to me. I am working with ArtForgeHub designers because I want something unique.

This site will be implemented with Wordpress using the Elementor framework,

About Me ---
I have worked with ArtForgeHub several times before, and I have tired to do everything I can to ve helpful. In the uploads, you will find PDF's with wireframes outlning the layout of the pages, as well as explanatios for each section. There are Word documents that you can copy into text. The list below explains the files included.

Although the wireframes suggest a layout, please feel free to use your creativity - often, I find that the designs I like the most are designs I have never thought of.

About the Company --
ERP (Enterprise Resource Planning) systems are business computer systems that tie different businesss functions together. These systems are expensive and complicated, and efforts to implement them often fail. The purpose of the company is to increase the chance of success by focusing on the things that need to be right.

I have uploaded several files to help clarify what I am looking for:
• 1a - Home Page Wireframe - PDF
Wireframe for the home page with an explanation of each section.
• 1b - Home Page Text – Word
A Word document so that you can copy the text.
• 2 - Copper Harbor Logo – ZIP
Four different versions of the company logo in Adobe Illustrator, PNG, and JPG formats. Any of the four are acceptable:
1. Logo_1 – Black on Transparent – Same Line ERP
2. Logo_2 – White on Transparent – Same Line ERP
3. Logo_3 – Black on Transparent – Big ERP on Different Line
4. Logo_4 – White on Transparent – Big ERP on Different Line
• 3a - Copper Harbor Page Wireframe – PDF
Wireframe for he Copper Harbor page, with explanations and a detailed breakdown of the top section.
• 3b - Copper Harbor Text – Word
• 4 - Colors and Palettes – PDF
• 5 - Change Management Icon – EPS
• 6 – Site Map
If you wish to see it, the site map provides an idea of the entire site. The two pages circled in red are the ones I need to be designed.

Thank you for your interest in this project!

Target Market(s)

Corporate decision makers, primarily CIOs and CFOs, as well as ERP project managers and influencers.

Industry/Entity Type

Consulting

Number of Pages Required

2 page

Font styles to use
Sans Serif

Requirements
Must have
• Pages that contain the elements explained on the wireframes provided.
Nice to have
• A design that looks and feels unique
Should not have
• A typical, template layour

```html
<!DOCTYPE html>
<html lang="en">
<head>
<meta charset="utf-8">
<title>Copper Harbor – ERP Project Consulting</title>
<link rel="stylesheet" href="https://fonts.googleapis.com/css2?family=Inter:wght@400;500;600;700;800&display=swap">
<style>
:root{
  --navy:#1f2540;
  --navy-deep:#161b30;
  --ink:#23283b;
  --muted:#6b7080;
  --page:#eef0f4;
  --white:#ffffff;
  --accent:#f0a83c;
  --hero-a:#3c4666;
  --hero-b:#7d879f;
  --line:#e2e4ea;
}
*{box-sizing:border-box;margin:0;padding:0}
html,body{width:673px;height:1200px;overflow:hidden}
body{font-family:"Inter",sans-serif;background:var(--page);color:var(--ink);position:relative}

/* header */
.site-header{position:absolute;left:0;top:0;width:673px;height:52px;background:var(--white);display:flex;align-items:center;padding:0 22px}
.brand{font-weight:700;font-size:15px;color:var(--navy);letter-spacing:-.2px}
.main-nav{display:flex;gap:26px;margin-left:auto;margin-right:22px}
.main-nav a{font-size:8px;font-weight:600;letter-spacing:.6px;text-transform:uppercase;color:var(--ink);text-decoration:none}
.search-icon{width:12px;height:12px;margin-right:18px}
.btn-header{background:var(--navy);color:var(--white);font-size:8px;font-weight:600;letter-spacing:.8px;text-transform:uppercase;padding:10px 17px;border-radius:16px}

/* hero */
.hero{position:absolute;left:0;top:52px;width:673px;height:350px;overflow:hidden}
.hero-photo{position:absolute;inset:0;background:linear-gradient(120deg,var(--hero-a) 0%,#55607e 45%,var(--hero-b) 100%)}
.hero-shade{position:absolute;inset:0;background:linear-gradient(180deg,rgba(31,37,64,.35),rgba(31,37,64,.55))}
.hero-content{position:absolute;left:0;right:0;top:48px;text-align:center;color:var(--white)}
.eyebrow{font-size:12px;font-weight:500;letter-spacing:.6px;text-transform:uppercase}
.hero-title{font-size:34px;font-weight:700;line-height:38px;letter-spacing:-.8px;margin:10px auto 0;width:470px}
.btn-hero{display:inline-flex;align-items:center;gap:8px;margin-top:22px;background:var(--white);color:var(--navy);font-size:8px;font-weight:600;letter-spacing:.8px;text-transform:uppercase;padding:12px 26px;border-radius:18px}

/* about */
.about{position:absolute;left:0;top:402px;width:673px;height:298px}
.about-band{position:absolute;left:412px;top:0;width:261px;height:34px;background:var(--white)}
.about-photo{position:absolute;left:26px;top:33px;width:268px;height:262px;border-radius:12px;background:linear-gradient(160deg,#6f7a93 0%,#3d4c74 55%,#25315a 100%);box-shadow:0 10px 24px rgba(31,37,64,.18)}
.about-label{position:absolute;left:13px;top:14px;font-size:17px;font-weight:700;color:var(--white)}
.about-label::after{content:"";display:block;width:46px;height:3px;background:var(--accent);margin-top:6px}
.about-card{position:absolute;left:325px;top:33px;width:348px;height:262px;background:var(--white);border-radius:10px 0 0 10px;padding:34px 26px 0 15px}
.about-title{font-size:14px;font-weight:600;line-height:22px;color:var(--ink)}
.about-tag{margin-top:12px;font-size:9px;font-weight:600;color:var(--accent)}
.about-text{margin-top:14px;font-size:8px;line-height:14px;color:#3b3f4f}
.stat-card{position:absolute;left:216px;top:203px;width:169px;height:77px;border-radius:8px;background:rgba(72,80,106,.92);display:flex;overflow:hidden;box-shadow:0 8px 18px rgba(0,0,0,.2)}
.stat-text{flex:1;padding:14px 0 0 11px;color:var(--white);font-size:8px;font-weight:600;line-height:13px;letter-spacing:.3px;text-transform:uppercase}
.stat-text small{display:block;font-weight:400;opacity:.75;margin-bottom:2px}
.stat-photo{width:86px;background:linear-gradient(180deg,#8c93a6,#2b2f3d)}
.btn-explore{position:absolute;left:388px;top:231px;width:114px;height:35px;border-radius:18px;background:var(--navy);color:var(--white);display:flex;align-items:center;justify-content:space-between;padding:0 14px;font-size:7px;font-weight:600;letter-spacing:.8px;text-transform:uppercase}

/* pursues */
.pursues{position:absolute;left:0;top:700px;width:673px;height:192px;text-align:center}
.pursues-title{margin-top:40px;font-size:23px;font-weight:600;color:var(--ink);letter-spacing:-.3px}
.pursues-lead{margin:12px auto 0;width:440px;font-size:18px;line-height:25px;font-weight:500;color:var(--ink);letter-spacing:-.2px}
.pursues-note{margin-top:16px;font-size:8px;color:var(--muted)}

/* services grid */
.services{position:absolute;left:0;top:892px;width:673px;height:308px;display:grid;grid-template-columns:repeat(4,1fr);grid-template-rows:repeat(2,1fr);gap:1px;background:var(--line)}
.service{background:var(--white);padding:24px 14px 0 18px}
.service-icon{width:22px;height:22px;border-radius:4px;background:#eceef2;display:flex;align-items:center;justify-content:center}
.service-title{margin-top:16px;font-size:12px;font-weight:700;color:var(--ink);letter-spacing:-.2px}
.service-text{margin-top:10px;font-size:7.5px;line-height:11.5px;color:#3b3f4f}
.portrait{display:block}
.portrait-a{background:linear-gradient(160deg,#3f4657,#a8b3c6)}
.portrait-b{background:linear-gradient(160deg,#b9c2cf,#dfe3ea)}
.portrait-c{background:linear-gradient(160deg,#7c8aa3,#2a3550)}
.portrait-d{background:linear-gradient(160deg,#c9ced6,#6f8bb0)}
</style>
</head>
<body>

<header class="site-header">
  <div class="brand">Copper Harbor</div>
  <nav class="main-nav">
    <a href="#">Home</a><a href="#">Agency</a><a href="#">Advice</a><a href="#">Company</a><a href="#">Contact</a>
  </nav>
  <svg class="search-icon" viewBox="0 0 12 12" aria-hidden="true"><circle cx="5" cy="5" r="3.6" fill="none" stroke="#555a6a" stroke-width="1.2"/><line x1="7.7" y1="7.7" x2="11" y2="11" stroke="#555a6a" stroke-width="1.2"/></svg>
  <div class="btn-header">Get Help</div>
</header>

<section class="hero">
  <div class="hero-photo" role="img" aria-label="Consultants meeting around laptops in a bright office"></div>
  <div class="hero-shade"></div>
  <div class="hero-content">
    <p class="eyebrow">Introduction</p>
    <h1 class="hero-title">Decades in pursuit of excellence in ERP solutions. Let us help you achieve ERP success.</h1>
    <div class="btn-hero">Get Started Here
      <svg width="6" height="7" viewBox="0 0 6 7" aria-hidden="true"><path d="M0 0L6 3.5L0 7Z" fill="#1f2540"/></svg>
    </div>
  </div>
</section>

<section class="about">
  <div class="about-band"></div>
  <div class="about-photo" role="img" aria-label="Portrait of the lead consultant in a navy suit">
    <span class="about-label">About</span>
  </div>
  <div class="about-card">
    <h2 class="about-title">Dana Whitlow, ERP Project Consultant, Introduces 25 Years in ERP Experience.</h2>
    <p class="about-tag">Trusted since day one</p>
    <p class="about-text">For over twenty years I have led ERP projects for finance, supply and operations teams. I know where projects fail and how to keep yours on the right path from plan to launch.</p>
  </div>
  <div class="stat-card">
    <div class="stat-text"><small>25 Years</small>ERP Workshops</div>
    <div class="stat-photo" role="img" aria-label="Consultant leading a workshop"></div>
  </div>
  <div class="btn-explore">
    <svg width="5" height="8" viewBox="0 0 5 8" aria-hidden="true"><path d="M4 1L1 4L4 7" fill="none" stroke="#fff" stroke-width="1.3"/></svg>
    Explore
    <svg width="5" height="8" viewBox="0 0 5 8" aria-hidden="true"><path d="M1 1L4 4L1 7" fill="none" stroke="#fff" stroke-width="1.3"/></svg>
  </div>
</section>

<section class="pursues">
  <h2 class="pursues-title">Pursues</h2>
  <p class="pursues-lead">We help at every stage to target ERP success, from groundwork to your go-live and continued stability.</p>
  <p class="pursues-note">⊙ Explore what drives our approach ⊙</p>
</section>

<section class="services">
  <article class="service">
    <div class="service-icon"><svg width="10" height="7" viewBox="0 0 10 7" aria-hidden="true"><rect x=".6" y=".6" width="8.8" height="5.8" rx="1" fill="none" stroke="#555a6a"/></svg></div>
    <h3 class="service-title">Risk Managing</h3>
    <p class="service-text">Clear change plans that bring every team along before the new system goes live.</p>
  </article>
  <article class="service">
    <div class="service-icon"><svg width="8" height="8" viewBox="0 0 8 8" aria-hidden="true"><path d="M2 1V7M6 1V7" stroke="#555a6a" stroke-width="1.2"/></svg></div>
    <h3 class="service-title">Vendor Deciding</h3>
    <p class="service-text">Guidance on vendors and partners so your choice fits the way you work.</p>
  </article>
  <div class="portrait portrait-a" role="img" aria-label="Smiling consultant in glasses at a desk"></div>
  <div class="portrait portrait-b" role="img" aria-label="Smiling consultant in a light blazer"></div>
  <div class="portrait portrait-c" role="img" aria-label="Senior advisor in a suit at an office desk"></div>
  <div class="portrait portrait-d" role="img" aria-label="Project lead in a blue shirt smiling"></div>
  <article class="service">
    <div class="service-icon"><svg width="10" height="6" viewBox="0 0 10 6" aria-hidden="true"><path d="M1 1H9M1 5H9" stroke="#555a6a" stroke-width="1.2"/></svg></div>
    <h3 class="service-title">Process Redesign</h3>
    <p class="service-text">Clean, mapped and tested data that keeps the launch on track.</p>
  </article>
  <article class="service">
    <div class="service-icon"><svg width="8" height="8" viewBox="0 0 8 8" aria-hidden="true"><path d="M2 1V4M6 1V4" stroke="#555a6a" stroke-width="1.2"/></svg></div>
    <h3 class="service-title">Live Post Coaching</h3>
    <p class="service-text">Hands-on support for project leads from kickoff to final sign-off.</p>
  </article>
</section>

</body>
</html>
```